Billboard design 8x3M NURA (Spanish company)

We´re located in the south of Spain. We run a local telecom company.
We sell Fiber optic, and mobile phone lines mainly.
The billboard will have to be in Spanish, I would like the price to be something you spot on first sight when passing by in the car.
Our company color is blue, like in our logo which I will add. I will also add a example from what we currently have.
The new offer should be:
1000 megas + 100Gigas movil con llamadas ilimitadas. (meaning 1000Mb fiber optic speed and 100Gb data and unlimited calls for 1 mobile line)
Our details are: phone line 952 00 0147
Website: nu-ra.es

```html
<!DOCTYPE html>
<html lang="es">
<head>
<meta charset="UTF-8">
<title>NURA – Valla 8x3</title>
<link href="https://fonts.googleapis.com/css2?family=Inter+Tight:wght@600;700;800&display=swap" rel="stylesheet">
<style>
  :root {
    --brand-blue: #1f4b86;
    --panel-blue-top: #214a80;
    --panel-blue-bottom: #3a67a2;
    --offer-red: #c81b33;
    --paper-top: #dededf;
    --paper-bottom: #ffffff;
    --white: #ffffff;
  }
  * { margin: 0; padding: 0; box-sizing: border-box; }
  html, body {
    width: 1200px; height: 727px; overflow: hidden;
    background: #ffffff;
    font-family: "Inter Tight", "Helvetica Neue", Arial, sans-serif;
  }
  .billboard {
    position: relative; width: 1200px; height: 727px; overflow: hidden;
    background: linear-gradient(180deg, var(--paper-top) 0%, var(--paper-bottom) 100%);
  }
  .offer-band {
    position: absolute; left: 0; top: 300px; width: 700px; height: 108px;
    background: var(--offer-red);
  }
  .offer-band__text {
    position: absolute; left: 48px; top: 326px;
    color: var(--white); font-weight: 700; font-size: 52px;
    letter-spacing: -1.5px; line-height: 1;
  }
  .headline {
    position: absolute; left: 44px; top: 62px;
    color: var(--brand-blue); font-weight: 800; font-size: 76px;
    line-height: 96px; letter-spacing: -3px;
  }
  .brand-panel { position: absolute; inset: 0; }
  .contact {
    position: absolute; left: 48px; color: var(--brand-blue);
    font-weight: 700; font-size: 74px; letter-spacing: -2.5px; line-height: 1;
    display: flex; align-items: center; gap: 30px;
  }
  .contact--phone { top: 494px; }
  .contact--web { top: 596px; }
  .contact__icon { width: 36px; height: 40px; flex: none; }
  .illustration {
    position: absolute; left: 680px; top: 200px; width: 470px; height: 470px;
    border-radius: 40px;
    background: radial-gradient(ellipse at 60% 55%, rgba(120,190,235,0.55) 0%, rgba(235,90,90,0.25) 45%, rgba(255,255,255,0) 72%);
  }
  .brand-mark {
    position: absolute; right: 70px; top: 56px; text-align: center;
    color: var(--white);
  }
  .brand-mark__name {
    font-weight: 800; font-size: 96px; letter-spacing: 2px; line-height: 1;
  }
  .brand-mark__services {
    margin-top: 16px; font-weight: 600; font-size: 26px; letter-spacing: 0;
  }
</style>
</head>
<body>
  <main class="billboard">
    <div class="offer-band"></div>

    <svg class="brand-panel" width="1200" height="727" viewBox="0 0 1200 727" aria-hidden="true">
      <defs>
        <linearGradient id="panelFill" x1="0" y1="0" x2="0" y2="1">
          <stop offset="0" stop-color="var(--panel-blue-top)"/>
          <stop offset="1" stop-color="var(--panel-blue-bottom)"/>
        </linearGradient>
      </defs>
      <path d="M596 0 C612 300 656 520 730 727 L1200 727 L1200 0 Z" fill="url(#panelFill)"/>
    </svg>

    <h1 class="headline">1000 megas +<br>100 Gigas movil</h1>
    <p class="offer-band__text">Con llamadas ilimitadas</p>

    <p class="contact contact--phone">
      <svg class="contact__icon" viewBox="0 0 40 44" aria-hidden="true">
        <path d="M6 2 L14 2 L16 12 L11 16 C13 24 18 30 25 33 L29 28 L38 31 L38 40 C38 42 36 43 34 43 C17 41 4 27 3 6 C3 4 4 2 6 2 Z" fill="var(--brand-blue)"/>
      </svg>
      952 00 0147
    </p>
    <p class="contact contact--web">
      <svg class="contact__icon" viewBox="0 0 40 44" aria-hidden="true">
        <path d="M4 4 L36 18 L22 22 L34 36 L29 41 L17 27 L10 38 Z" fill="var(--brand-blue)"/>
      </svg>
      nu-ra.es
    </p>

    <div class="illustration" role="img" aria-label="Ilustración de haces de fibra óptica de colores entrando en un monitor de ordenador"></div>

    <div class="brand-mark">
      <div class="brand-mark__name">NURA</div>
      <div class="brand-mark__services">Wifi | Fibra | Movil | Tv</div>
    </div>
  </main>
</body>
</html>
```